Endocrinologist needs new stationery

I have a logo from MarkForge and now need stationery with the new logo.

Address: Suite 4, 282 Falcon Street, Richmond, VIC 3121
Phone: 03 9417 2253
Fax: 03 9417 2255
Website: www.drmaylacorwen.com.au
Email: admin@drmaylacorwen.com.au

```html
<!DOCTYPE html>
<html lang="en">
<head>
<meta charset="utf-8">
<title>Dr Mayla Corwen Endocrinology – Letterhead</title>
<link rel="stylesheet" href="https://fonts.googleapis.com/css2?family=EB+Garamond:wght@400;500;600&display=swap">
<style>
  :root {
    --backdrop: #e2e2e2;
    --paper: #ffffff;
    --brand-blue: #316c9a;
    --brand-plum: #74505f;
    --ink: #1a1a1a;
  }
  * { margin: 0; padding: 0; box-sizing: border-box; }
  html, body { width: 977px; height: 1200px; overflow: hidden; }
  body {
    background: var(--backdrop);
    font-family: "EB Garamond", Georgia, serif;
    position: relative;
  }
  .letterhead {
    position: absolute;
    left: 122px;
    top: 83px;
    width: 730px;
    height: 1033px;
    background: var(--paper);
    overflow: hidden;
  }
  .brand-name {
    position: absolute;
    left: 46px;
    top: 82px;
    font-size: 40px;
    font-weight: 400;
    color: var(--brand-blue);
    line-height: 1;
    white-space: nowrap;
  }
  .header-divider {
    position: absolute;
    left: 458px;
    top: 49px;
    width: 2px;
    height: 96px;
    background: var(--brand-plum);
  }
  .contact-block {
    position: absolute;
    left: 478px;
    top: 48px;
    color: var(--ink);
    font-size: 13.5px;
    line-height: 1.15;
  }
  .contact-row {
    display: flex;
    align-items: flex-start;
    gap: 8px;
    margin-bottom: 4px;
  }
  .contact-row svg { flex: none; width: 10px; height: 12px; margin-top: 2px; fill: var(--brand-blue); }
  .contact-row.address { margin-bottom: 6px; }
  .practice-name { font-weight: 600; }
  .page-footer {
    position: absolute;
    left: 0;
    bottom: 0;
    width: 730px;
    height: 130px;
  }
  .page-footer svg { display: block; }
  .website {
    position: absolute;
    left: 0;
    right: 0;
    bottom: 14px;
    text-align: center;
    color: #fff;
    font-size: 15px;
    letter-spacing: 2.4px;
    font-weight: 500;
  }
</style>
</head>
<body>
  <main class="letterhead">
    <header>
      <div class="brand-name">Dr Mayla Corwen</div>
      <div class="header-divider"></div>
      <address class="contact-block" style="font-style:normal">
        <div class="contact-row address">
          <svg viewBox="0 0 10 12"><path d="M5 0a4 4 0 0 0-4 4c0 3 4 8 4 8s4-5 4-8a4 4 0 0 0-4-4zm0 5.6a1.6 1.6 0 1 1 0-3.2 1.6 1.6 0 0 1 0 3.2z"/></svg>
          <div><span class="practice-name">DrMaylaCorwen Endocrinology</span><br>Suite 4, 282 Falcon Street<br>Richmond, VIC 3121</div>
        </div>
        <div class="contact-row">
          <svg viewBox="0 0 10 12"><path d="M2 2l2-1 1.5 3-1.2.9c.6 1.4 1.4 2.3 2.6 3l1-1.1L10 8.5 9 10.5C5 10.5 1.5 6.5 2 2z"/></svg>
          <span>03 9417 2253</span>
        </div>
        <div class="contact-row">
          <svg viewBox="0 0 10 12"><path d="M2.5 2h5v2.5h-5zM1 5h8v4H7.5V7.5h-5V9H1zM3 8h4v3H3z"/></svg>
          <span>03 9417 2255</span>
        </div>
        <div class="contact-row">
          <svg viewBox="0 0 10 12"><path d="M0 3h10v6H0zm.8.6L5 6.6l4.2-3z" fill-rule="evenodd"/></svg>
          <span>admin@drmaylacorwen.com.au</span>
        </div>
      </address>
    </header>
    <footer class="page-footer">
      <svg width="730" height="130" viewBox="0 0 730 130" aria-hidden="true">
        <path d="M0 40 C 200 76 430 90 680 70 C 430 84 200 78 0 24 Z" fill="var(--brand-plum)"/>
        <path d="M0 46 C 220 84 450 98 730 60 L730 130 L0 130 Z" fill="var(--brand-blue)"/>
      </svg>
      <div class="website">WWW.DRMAYLACORWEN.COM.AU</div>
    </footer>
  </main>
</body>
</html>
```